Fernhollow Ridge Farms
letterhead, envelope and business cards
Fernhollow Ridge Farms -
Creative Brief
Traditional
Tessa Harlan
3157 W Birch Mill Road North Platte, NE 68437
sales@fernhollowridgefarms.example
www.fernhollowridgefarms.example

```html
<!DOCTYPE html>
<html lang="en">
<head>
<meta charset="utf-8">
<title>Fernhollow Ridge Farms – Stationery</title>
<link rel="stylesheet" href="https://fonts.googleapis.com/css2?family=Arimo:wght@400;700&display=swap">
<style>
  :root {
    --board: #6d6d6d;
    --board-edge: #3e3e3e;
    --paper: #ffffff;
    --brown: #7a4b1c;
    --brown-dark: #5e3812;
    --window: #e4e4e4;
    --card-grey-1: #f4f4f4;
    --card-grey-2: #c9c9c9;
    --faint: rgba(122, 75, 28, 0.12);
  }
  * { box-sizing: border-box; margin: 0; padding: 0; }
  html, body { width: 1200px; height: 737px; overflow: hidden; }
  body {
    font-family: "Arimo", Arial, sans-serif;
    background: var(--board);
    border: 6px solid var(--board-edge);
    position: relative;
  }
  .piece { position: absolute; overflow: hidden; box-shadow: 0 2px 6px rgba(0,0,0,.35); }
  .wordmark {
    color: var(--brown);
    font-weight: 700;
    text-align: center;
    line-height: 1.05;
    display: flex; align-items: center; justify-content: center; gap: 10px;
  }
  .wordmark .dot { width: 14px; height: 14px; border-radius: 50%; background: var(--brown); flex: none; }
  .band { position: absolute; left: 0; width: 100%; }
  .band svg { display: block; width: 100%; height: 100%; }

  /* Letterhead top */
  .letterhead-top { left: 30px; top: 6px; width: 576px; height: 232px; background: var(--paper); }
  .letterhead-top .wordmark { position: absolute; top: 22px; left: 0; right: 0; font-size: 30px; }

  /* Envelope */
  .envelope { left: 24px; top: 227px; width: 600px; height: 247px; background: var(--paper); }
  .envelope .flap { top: 0; height: 62px; }
  .envelope .wordmark { position: absolute; left: 16px; top: 48px; font-size: 20px; justify-content: flex-start; }
  .envelope .window {
    position: absolute; left: 329px; top: 108px; width: 185px; height: 72px;
    background: var(--window); border-radius: 8px; box-shadow: inset 0 1px 3px rgba(0,0,0,.15);
  }
  .envelope .footer { bottom: 0; height: 44px; }
  .envelope .address {
    position: absolute; left: 16px; bottom: 12px; color: #fff; font-size: 13px; font-weight: 700;
  }

  /* Letterhead bottom */
  .letterhead-bottom { left: 24px; top: 474px; width: 600px; height: 245px; background: var(--paper); }
  .letterhead-bottom .watermark {
    position: absolute; left: 230px; top: 6px; width: 330px; height: 120px;
    background: radial-gradient(ellipse at center, var(--faint), rgba(122,75,28,0) 70%);
  }
  .letterhead-bottom .footer { bottom: 0; height: 84px; }
  .letterhead-bottom .contact {
    position: absolute; left: 0; right: 0; bottom: 10px; text-align: center;
    color: #fff; font-size: 11px; line-height: 1.6;
  }

  /* Card front */
  .card-front { left: 642px; top: 47px; width: 533px; height: 307px; background: var(--paper); }
  .card-front .name { position: absolute; left: 18px; top: 18px; color: var(--brown); font-size: 29px; font-weight: 700; }
  .card-front .wordmark { position: absolute; left: 0; right: 0; top: 100px; font-size: 40px; }
  .card-front .details {
    position: absolute; left: 60px; right: 20px; top: 196px; text-align: center;
    color: var(--brown-dark); font-size: 13px; font-weight: 700; line-height: 1.35;
  }
  .card-front .footer { bottom: 0; height: 48px; }

  /* Card back */
  .card-back {
    left: 642px; top: 378px; width: 533px; height: 336px;
    background: radial-gradient(ellipse at 50% 45%, var(--card-grey-1), var(--card-grey-2));
  }
  .card-back .wordmark { position: absolute; left: 0; right: 0; top: 112px; font-size: 42px; }
  .card-back .web {
    position: absolute; left: 0; right: 0; top: 222px; text-align: center;
    color: var(--brown); font-size: 17px; font-weight: 700;
  }
</style>
</head>
<body>

<section class="piece letterhead-top" aria-label="Letterhead, top">
  <div class="wordmark"><span class="dot"></span>Fernhollow Ridge Farms</div>
</section>

<section class="piece envelope" aria-label="Envelope">
  <div class="band flap">
    <svg viewBox="0 0 600 62" preserveAspectRatio="none"><path d="M0 0H600V30Q300 70 0 30Z" fill="var(--brown)"/></svg>
  </div>
  <div class="wordmark"><span class="dot"></span>Fernhollow Ridge Farms</div>
  <div class="window"></div>
  <div class="band footer">
    <svg viewBox="0 0 600 44" preserveAspectRatio="none"><path d="M0 8Q300 -6 600 8V44H0Z" fill="var(--brown)"/></svg>
  </div>
  <p class="address">3157 W Birch Mill Road, North Platte, NE 68437</p>
</section>

<section class="piece letterhead-bottom" aria-label="Letterhead, bottom">
  <div class="watermark" role="img" aria-label="Faint farm name watermark"></div>
  <div class="band footer">
    <svg viewBox="0 0 600 84" preserveAspectRatio="none"><path d="M0 20Q300 -14 600 20V84H0Z" fill="var(--brown)"/></svg>
  </div>
  <p class="contact">3157 W Birch Mill Road, North Platte, NE 68437 PH: 308-555-0142<br>E-mail: sales@fernhollowridgefarms.example www.fernhollowridgefarms.example</p>
</section>

<section class="piece card-front" aria-label="Business card, front">
  <h1 class="name">Tessa Harlan</h1>
  <div class="wordmark"><span class="dot"></span>Fernhollow Ridge Farms</div>
  <p class="details">3157 W Birch Mill Road, North Platte, NE 68437<br>PH: 308-555-0142 E-mail: sales@fernhollowridgefarms.example<br>www.fernhollowridgefarms.example</p>
  <div class="band footer">
    <svg viewBox="0 0 533 48" preserveAspectRatio="none"><path d="M0 14Q266 -8 533 14V48H0Z" fill="var(--brown)"/></svg>
  </div>
</section>

<section class="piece card-back" aria-label="Business card, back">
  <div class="wordmark"><span class="dot"></span>Fernhollow Ridge Farms</div>
  <p class="web">www.fernhollowridgefarms.example</p>
</section>

</body>
</html>
```